New Business Card Design Project

I need a design for business cards, i am an electrical business called "Tandor Electrical and Communications" i need the cards to be double sided with the company logo on the back (attached) the front needs to say my company name, web site, email address, telephone number, and ABN number and electrical license number. I am open to different arrangements of the information but would like the background to be incorporating something electrical or something that looks smart. open to all additional ideas also.

The company colours are orange and grey see logo attached.

Business Name: Tandor Electrical and Communications
Website: tandorelectricalandcomms.example.au
Email: brent@tandorelectricalandcomms.example.au
Telephone(mobile): 0481203967
ABN: 71829034618
Lic No: 830472F

Target Market(s)

Business entities, Project Managers, Accounts, Clients

Industry/Entity Type

Electrician

Contact Information for Business Card

I need a design for business cards, i am an electrical business called "Tandor Electrical and Communications" i need the cards to be double sided with the company logo on the back (attached) the front needs to say my company name

Font styles to use
Serif
Sans Serif

Colors
f37122
5c5c5c

Requirements
Must have
• Must have the Logo on the back open to different ways of it being on the back but had in mind to keep it central but again open to other options
Nice to have
• A real modern cool background that is eye catching yet contemporary
Should not have
• No backgrounds of a light bulb or plug or anything like that

```html
<!DOCTYPE html>
<html lang="en">
<head>
<meta charset="utf-8">
<title>Tandor Electrical and Communications – Business Card</title>
<link rel="stylesheet" href="https://fonts.googleapis.com/css2?family=Open+Sans:wght@400;600;700&display=swap">
<style>
  :root {
    --stage: #e7e4e1;
    --card-black: #000000;
    --amber: #f9ae1b;
    --white: #ffffff;
    --ink: #111111;
  }
  * { margin: 0; padding: 0; box-sizing: border-box; }
  html, body { width: 1200px; height: 900px; overflow: hidden; }
  body {
    position: relative;
    background: var(--stage);
    font-family: "Open Sans", Arial, sans-serif;
  }
  .card {
    position: absolute;
    width: 556px;
    height: 342px;
    overflow: hidden;
    box-shadow: 0 6px 18px rgba(0,0,0,0.25);
  }
  .card--front { left: 237px; top: 62px; background: var(--amber); }
  .card--back { left: 457px; top: 519px; width: 560px; background: var(--card-black); }

  .front__header {
    position: absolute; left: 0; top: 0; width: 100%; height: 150px;
    background: var(--card-black);
  }
  .front__decor {
    position: absolute; left: 0; top: 110px; width: 100%; height: 130px;
    background: linear-gradient(180deg, var(--card-black) 0%, var(--card-black) 25%, var(--amber) 100%);
  }
  .holder {
    position: absolute; left: 0; top: 22px; width: 100%;
    text-align: center; color: var(--white);
  }
  .holder__name { font-size: 20px; font-weight: 700; letter-spacing: 0.3px; }
  .holder__role { font-size: 14px; font-weight: 400; margin-top: 2px; }

  .contact {
    position: absolute; left: 33px; top: 243px;
    list-style: none; color: var(--ink); font-size: 14.5px; line-height: 21px;
  }
  .contact li { display: flex; align-items: center; gap: 8px; }
  .contact svg { width: 11px; height: 11px; fill: var(--ink); flex: none; }

  .registration {
    position: absolute; right: 28px; top: 262px;
    text-align: right; color: var(--ink); font-size: 14.5px; line-height: 21px;
  }

  .brand {
    position: absolute; left: 0; top: 140px; width: 100%;
    display: flex; flex-direction: column; align-items: center;
    color: var(--amber); font-weight: 600;
  }
  .brand__name { font-size: 50px; letter-spacing: 6px; line-height: 1; }
  .brand__sub { font-size: 15px; letter-spacing: 1.6px; margin-top: 12px; }
</style>
</head>
<body>

  <section class="card card--front" aria-label="Business card front">
    <div class="front__header"></div>
    <div class="front__decor" role="img" aria-label="Flowing electrical cable wave artwork"></div>

    <div class="holder">
      <p class="holder__name">DALE HARPER</p>
      <p class="holder__role">Director</p>
    </div>

    <ul class="contact">
      <li>
        <svg viewBox="0 0 24 24" aria-hidden="true"><path d="M6.6 10.8a15.1 15.1 0 0 0 6.6 6.6l2.2-2.2c.3-.3.7-.4 1-.2 1.1.4 2.3.6 3.6.6.6 0 1 .4 1 1V20c0 .6-.4 1-1 1A17 17 0 0 1 3 4c0-.6.4-1 1-1h3.5c.6 0 1 .4 1 1 0 1.2.2 2.4.6 3.6.1.3 0 .7-.2 1z"/></svg>
        0481203967
      </li>
      <li>
        <svg viewBox="0 0 24 24" aria-hidden="true"><path d="M2 5h20v14H2z M2 5l10 8 10-8" /></svg>
        brent@tandorelectricalandcomms.example.au
      </li>
      <li>
        <svg viewBox="0 0 24 24" aria-hidden="true"><circle cx="12" cy="12" r="10"/></svg>
        tandorelectricalandcomms.example.au
      </li>
    </ul>

    <div class="registration">
      <p>ABN: 71829034618</p>
      <p>Lic No: 830472F</p>
    </div>
  </section>

  <section class="card card--back" aria-label="Business card back">
    <div class="brand">
      <p class="brand__name">TANDOR</p>
      <p class="brand__sub">ELECTRICAL &amp; COMMUNICATIONS</p>
    </div>
  </section>

</body>
</html>
```